Borealith Homepage Design

We need a home page design for Borealith. Borealith creates gear for outdoor enthusiasts who are passionate about conservation, wildlife observation, and ethical hunting.

Current Website: www.borealkit.com

Customer Avatar Canvas:
https://sheets.plantodeck.com/d/7XqRmTz4LkWp9VbNc2HsYd8JfGa3UeQo5iKtZrMn/edit#gid=90352114

Homepage Template: Attached below
https://files.plantodeck.com/folders/8kT3zQwLm5RpVx2NbYc7HdJf4GaUeWo

There is info on imagery in the homepage template. Where there isn't, appropriate stock imagery is acceptable.

Logo Design and Product Images: https://files.plantodeck.com/folders/3wR9yHnKb6TmQz4LpXv2CdFg8JsAeUo

```html
<!DOCTYPE html>
<html lang="en">
<head>
<meta charset="utf-8">
<title>Borealith – Home</title>
<link href="https://fonts.googleapis.com/css2?family=Plus+Jakarta+Sans:wght@300;400;500;600;700;800&family=Oswald:wght@500&display=swap" rel="stylesheet">
<style>
:root{
  --green:#0fbf4f;
  --green-line:#2fc764;
  --mint:#e9fcef;
  --ink:#111111;
  --body:#3a3a3a;
  --white:#ffffff;
  --black:#000000;
  --grey-logo:#9b9b9b;
}
*{margin:0;padding:0;box-sizing:border-box}
html,body{width:1200px;height:3529px;overflow:hidden}
body{position:relative;background:var(--white);font-family:"Plus Jakarta Sans",sans-serif;color:var(--ink)}
.abs{position:absolute}

/* header */
.site-header{left:0;top:0;width:1200px;height:93px;background:var(--white)}
.brand{left:110px;top:28px;display:flex;align-items:center;gap:10px;font-size:24px;font-weight:700;color:var(--ink)}
.brand-mark{width:28px;height:28px;border-radius:50%;background:var(--ink)}
.nav-link{top:36px;font-size:14px;font-weight:500;color:var(--ink)}
.nav-link.active::after{content:"";position:absolute;left:0;right:0;top:31px;height:2px;background:var(--green)}
.btn{display:flex;align-items:center;justify-content:center;text-align:center;font-size:10px;font-weight:700;line-height:1.2;text-transform:uppercase;color:var(--white);background:var(--green);border-radius:3px}
.header-cta{left:877px;top:26px;width:212px;height:38px;font-size:9px}

/* hero */
.hero{left:0;top:93px;width:1200px;height:607px;background:linear-gradient(160deg,#8a8f86 0%,#4d5a40 35%,#2f3a28 65%,#3c3f38 100%)}
.hero-title{left:108px;top:248px;color:var(--white);font-weight:300;font-size:40px;line-height:45px;letter-spacing:-.3px}
.hero-title b{font-weight:800;font-size:45px}
.btn-outline{height:46px;width:240px;border:1.5px solid var(--green);background:transparent;border-radius:2px;top:463px}

/* section titles */
.section-title{left:0;width:1200px;text-align:center;font-size:33px;font-weight:500}
.section-title::after{content:"";display:block;width:46px;height:3px;background:var(--green);margin:8px auto 0}

/* partners */
.partner{top:872px;width:84px;height:60px;background:var(--grey-logo);opacity:.55}

/* video */
.video-band{left:0;top:1029px;width:1200px;height:559px;background:var(--mint)}
.video{left:274px;top:1110px;width:652px;height:312px;border-radius:2px;overflow:hidden;background:linear-gradient(180deg,#6c7a55 0%,#4f5b3b 55%,#3a3b33 100%)}
.video-label{left:16px;top:14px;font-family:"Oswald",sans-serif;font-size:12px;color:var(--white);letter-spacing:.3px}
.video-bar{left:0;bottom:0;width:652px;height:48px;background:linear-gradient(0deg,rgba(0,0,0,.75),rgba(0,0,0,0))}
.video-cta{left:479px;top:1456px;width:240px;height:46px}

/* how it works */
.subtitle{left:0;top:1729px;width:1200px;text-align:center;font-size:15px;font-weight:500;line-height:18px}
.timeline{left:600px;top:1892px;width:1.5px;height:673px;background:var(--green-line)}
.step-num{width:31px;height:31px;border-radius:50%;border:1.5px solid var(--green-line);background:var(--white);color:var(--green);font-size:14px;display:flex;align-items:center;justify-content:center;left:585px}
.photo{width:311px;height:184px;border-radius:2px}
.step{width:325px}
.step h3{font-size:13px;font-weight:600;line-height:16px;margin-bottom:10px}
.step p{font-size:11.5px;line-height:18px;color:var(--body)}

/* testimonials */
.clients{left:0;top:2756px;width:1200px;height:576px;background:var(--black)}
.clients .section-title{color:var(--white);top:94px}
.review-card{left:110px;top:203px;width:233px;height:160px;background:var(--white);border-radius:2px}
.review-avatar{left:15px;top:14px;width:28px;height:28px;border-radius:50%;background:#c4c4c4}
.review-rule{left:0;top:73px;width:233px;height:1px;background:#dddddd}
.continue{left:0;top:3412px;width:1255px;text-align:center;font-size:38px;font-weight:400}
</style>
</head>
<body>

<header class="abs site-header">
  <div class="abs brand"><span class="brand-mark"></span>Borealith</div>
  <nav>
    <span class="abs nav-link active" style="left:588px">Features</span>
    <span class="abs nav-link" style="left:689px">About Us</span>
    <span class="abs nav-link" style="left:794px">Log In</span>
  </nav>
  <a class="abs btn header-cta">Unlock the power of optics<br>and preserve the wild</a>
</header>

<section class="abs hero" role="img" aria-label="Hikers with backpacks climbing a rocky mountain trail in a green valley"></section>
<h1 class="abs hero-title"><b>Explore The</b> Wild West<br>Embrace Conservation, Hunt<br>Ethically, And Protect Public<br>Lands With <b>Borealith Gear</b></h1>
<a class="abs btn btn-outline" style="left:110px">Order your Borealith<br>bino harness today!</a>
<a class="abs btn btn-outline" style="left:359px">Unlock the power of optics<br>and preserve the wild</a>

<h2 class="abs section-title" style="top:790px">Trusted By</h2>
<div class="abs partner" style="left:119px;border-radius:8px"></div>
<div class="abs partner" style="left:288px;clip-path:polygon(50% 0,100% 100%,0 100%)"></div>
<div class="abs partner" style="left:455px;width:60px;border-radius:50%"></div>
<div class="abs partner" style="left:608px;width:60px;border-radius:6px"></div>
<div class="abs partner" style="left:758px;width:104px;border-radius:4px"></div>
<div class="abs partner" style="left:946px;width:140px;border-radius:30px"></div>

<section class="abs video-band"></section>
<div class="abs video" role="img" aria-label="Video thumbnail of a hiker walking across a log bridge in a forest">
  <span class="abs video-label">CLICK &amp; WATCH NOW OUR VIDEO</span>
  <svg class="abs" style="left:296px;top:116px" width="60" height="60" viewBox="0 0 60 60">
    <circle cx="30" cy="30" r="28" fill="none" stroke="#fff" stroke-opacity=".5" stroke-width="2"/>
    <circle cx="30" cy="30" r="22" fill="#fff"/>
    <path d="M25 20 L40 30 L25 40Z" fill="var(--green)"/>
  </svg>
  <div class="abs video-bar"></div>
  <svg class="abs" style="left:0;top:264px" width="652" height="48" viewBox="0 0 652 48">
    <rect x="13" y="12" width="626" height="2" fill="#fff" fill-opacity=".35"/>
    <rect x="13" y="12" width="146" height="2" fill="#fff"/>
    <rect x="14" y="23" width="3" height="10" fill="#fff"/><rect x="20" y="23" width="3" height="10" fill="#fff"/>
    <path d="M36 23 L43 28 L36 33Z M44 23 h2 v10 h-2Z" fill="#fff"/>
    <path d="M60 25 h3 l4 -3 v12 l-4 -3 h-3Z" fill="#fff"/>
    <text x="84" y="31" font-size="7" fill="#fff" font-family="Plus Jakarta Sans, sans-serif">0:35 / 2:25</text>
    <rect x="552" y="25" width="11" height="7" fill="#fff"/>
    <circle cx="583" cy="28" r="5" fill="none" stroke="#fff" stroke-width="2"/>
    <rect x="598" y="24" width="12" height="9" fill="none" stroke="#fff" stroke-width="2"/>
    <path d="M621 23 h4 M621 23 v4 M634 23 h-4 M634 23 v4 M621 34 h4 M621 34 v-4 M634 34 h-4 M634 34 v-4" stroke="#fff" stroke-width="2"/>
  </svg>
</div>
<a class="abs btn video-cta">Order your Borealith<br>bino harness today!</a>

<h2 class="abs section-title" style="top:1666px">How It Works</h2>
<p class="abs subtitle">Introducing The Borealith Bino Harness – The Ultimate<br>Companion For Your Optics</p>

<div class="abs timeline"></div>
<div class="abs step-num" style="top:1876px">1</div>
<div class="abs step-num" style="top:2101px">2</div>
<div class="abs step-num" style="top:2324px">3</div>
<div class="abs step-num" style="top:2549px">4</div>

<div class="abs photo" style="left:210px;top:1800px;background:linear-gradient(135deg,#d9c88a,#7b7a3c 50%,#3d4624)" role="img" aria-label="Two hikers with backpacks walking on a grassy coastal cliff at sunset"></div>
<div class="abs step" style="left:673px;top:1828px">
  <h3>STEP 1: Experience unparalleled convenience and comfort during your outdoor excursions with the Borealith Bino Harness</h3>
  <p>Designed specifically for the modern conservationist and avid hunter, this innovative harness combines functionality, durability, and style to enhance your wildlife observation and hunting experiences.</p>
</div>

<div class="abs step" style="left:210px;top:2034px">
  <h3>STEP 2: Unmatched Optics Protection:</h3>
  <p>Our Bino Harness features a secure and adjustable harness system that keeps your binoculars safe and within easy reach at all times. No more fumbling around or worrying about accidentally dropping your expensive optics. With the Borealith Bino Harness, your binoculars are securely strapped to your chest, offering quick and hassle-free access whenever you need them.</p>
</div>
<div class="abs photo" style="left:680px;top:2023px;background:linear-gradient(135deg,#8e8a7c,#5d6b4a 50%,#a04a3a)" role="img" aria-label="Climber in a helmet and harness on a rocky cliff above a green valley"></div>

<div class="abs photo" style="left:210px;top:2248px;background:linear-gradient(135deg,#3c3a2c,#6a4a32 50%,#2e4a3a)" role="img" aria-label="Hand resting on a deer antler among ferns"></div>
<div class="abs step" style="left:673px;top:2256px">
  <h3>STEP 3: Thoughtful Design for Easy Access:</h3>
  <p>We've incorporated thoughtful design elements into the Borealith Bino Harness to enhance your outdoor adventures. The quick-release buckles allow for swift and effortless removal of the harness, granting you unhindered mobility when necessary. The adjustable straps ensure a personalized fit for individuals of all body types, providing a secure and snug grip on your binoculars.</p>
</div>

<div class="abs step" style="left:210px;top:2482px">
  <h3>STEP 4: Embrace Conservation:</h3>
  <p>By choosing the Borealith Bino Harness, you're not only investing in a premium gear accessory but also supporting the conservation of public lands and wildlife. We are dedicated to promoting sustainable hunting and ethical practices, and a portion of the proceeds from every purchase goes towards initiatives that preserve the habitats we hold dear.</p>
</div>
<div class="abs photo" style="left:680px;top:2471px;background:linear-gradient(135deg,#e8d79a,#7f9a3c 45%,#3b4a2c)" role="img" aria-label="Group of volunteers in high-visibility vests standing arm in arm in a sunlit forest"></div>

<section class="abs clients">
  <h2 class="abs section-title">What Our Clients Say</h2>
  <div class="abs review-card">
    <div class="abs review-avatar"></div>
    <div class="abs review-rule"></div>
  </div>
</section>

<p class="abs continue">continue....</p>

</body>
</html>
```